Vesmor Herbal Products label packaging for my skin and hair line

I need labels thats Clear & attractive, calm & catchy. I have attached some label pictures from pixel forge designers that I like to give an idea of what I expect. I have also attached pictures of my currebt labels which are not bad however I would like better labels

Target Market(s)

People with natural hair & those who love natural products

Industry/Entity Type

Hair And Beauty

Colors

Designer to choose only greyscale colors for use in the design.

Requirements
Must have
• Beautifull fonts & patterns.
Nice to have
• Black &white colours.
Mint is brand color
Should not have
• Should not have pictures of people, shapes or images

```html
<!DOCTYPE html>
<html lang="en">
<head>
<meta charset="utf-8">
<title>Vesmor Herbal – Label Set</title>
<link rel="stylesheet" href="https://fonts.googleapis.com/css2?family=Montserrat:wght@300;400;500;600&family=Allura&display=swap">
<style>
  :root {
    --bg-light: #f4f4f4;
    --bg-dark: #dcdcdc;
    --mint: #a9dcc8;
    --mint-pale: #d3ece0;
    --mint-text: #8fd1b8;
    --lilac-pale: #efe6ef;
    --pack-yellow: #f3d473;
    --pack-grey: #d2d2d4;
    --dropper-white: #ffffff;
    --ink: #1d1d1d;
    --teal-dark: #1f3d3b;
    --gold: #f0b232;
    --sky: #35b3e0;
    --paper: #ffffff;
  }
  * { margin: 0; padding: 0; box-sizing: border-box; }
  html, body { width: 956px; height: 1200px; overflow: hidden; }
  body {
    position: relative;
    background: radial-gradient(ellipse at 50% 50%, var(--bg-light) 0%, var(--bg-dark) 100%);
    font-family: "Montserrat", sans-serif;
    color: var(--ink);
  }
  .abs { position: absolute; }

  /* packaging shapes */
  .dropper-bulb { left: 452px; top: 29px; width: 55px; height: 120px; background: var(--dropper-white); border-radius: 28px 28px 4px 4px; }
  .dropper-collar { left: 427px; top: 145px; width: 105px; height: 83px; background: var(--pack-yellow); border-radius: 4px; }
  .bottle-neck { left: 438px; top: 226px; width: 83px; height: 20px; background: var(--pack-yellow); }
  .bottle-shoulder { left: 398px; top: 244px; width: 163px; height: 90px; background: var(--pack-yellow); border-radius: 70px 70px 0 0; }
  .bottle-base { left: 398px; top: 520px; width: 163px; height: 34px; background: var(--pack-yellow); border-radius: 0 0 14px 14px; }
  .jar-lid { left: 345px; top: 583px; width: 280px; height: 73px; background: var(--pack-yellow); border-radius: 5px; }
  .jar-body { left: 343px; top: 656px; width: 285px; height: 180px; background: var(--pack-grey); border-radius: 12px 12px 8px 8px; }

  /* labels */
  .label { position: absolute; background: var(--paper); overflow: hidden; }
  .foliage { position: absolute; background: linear-gradient(100deg, var(--mint-pale) 0%, var(--lilac-pale) 45%, var(--mint-pale) 75%, var(--lilac-pale) 100%); opacity: .9; }
  .edge-line { position: absolute; left: 0; right: 0; height: 4px; background: var(--mint-pale); }
  .brand-dot { position: absolute; border-radius: 50%; background: var(--teal-dark); box-shadow: 0 0 0 3px var(--mint-pale); }
  .brand-name { position: absolute; font-weight: 300; letter-spacing: .28em; text-transform: uppercase; color: var(--teal-dark); white-space: nowrap; }
  .title-script { position: absolute; font-family: "Allura", cursive; white-space: nowrap; text-align: center; line-height: 1; }
  .centered { text-align: center; white-space: nowrap; position: absolute; }
  .tab { position: absolute; background: var(--mint); border-radius: 8px 8px 0 0; text-align: center; font-weight: 500; color: var(--ink); }
  .copy p { margin-bottom: 1em; }
  .copy h4 { color: var(--mint-text); font-weight: 600; }
  .fine { position: absolute; font-size: 4.6px; line-height: 1.2; font-weight: 500; }

  /* oil label */
  .label--oil { left: 245px; top: 322px; width: 467px; height: 205px; }
  .label--oil .copy { position: absolute; font-size: 6.2px; line-height: 1.3; font-weight: 500; }
  .label--oil .copy--left { left: 10px; top: 44px; width: 127px; text-align: center; }
  .label--oil .copy--right { left: 341px; top: 45px; width: 115px; text-align: center; }
  .label--oil .copy--right p { margin-bottom: 0; }

  /* jar wrap label */
  .label--jar { left: 31px; top: 679px; width: 894px; height: 149px; }
  .label--jar .copy { position: absolute; font-size: 7px; line-height: 1.25; font-weight: 500; }
  .label--jar .copy--mid { left: 157px; top: 40px; width: 202px; }
  .label--jar .copy--right { left: 558px; top: 34px; width: 330px; }
  .label--jar .copy--right p { margin-bottom: 0; }

  /* lid label */
  .label--lid { left: 351px; top: 864px; width: 270px; height: 270px; border-radius: 50%; box-shadow: inset 0 0 0 5px var(--mint-pale); }
  .lid-foliage { position: absolute; inset: 5px; border-radius: 50%; background: radial-gradient(circle, transparent 58%, var(--lilac-pale) 66%, var(--mint-pale) 80%, var(--lilac-pale) 100%); }
</style>
</head>
<body>

  <!-- dropper bottle -->
  <div class="abs dropper-bulb"></div>
  <div class="abs dropper-collar"></div>
  <div class="abs bottle-neck"></div>
  <div class="abs bottle-shoulder"></div>
  <div class="abs bottle-base"></div>

  <section class="label label--oil">
    <div class="foliage" style="left:0;top:0;width:180px;height:40px" role="img" aria-label="Line-drawn tropical leaves in mint and lilac"></div>
    <div class="foliage" style="right:0;top:0;width:180px;height:40px" role="img" aria-label="Line-drawn tropical leaves in mint and lilac"></div>
    <div class="foliage" style="left:0;bottom:0;width:170px;height:38px" role="img" aria-label="Line-drawn tropical leaves in mint and lilac"></div>
    <div class="foliage" style="right:0;bottom:0;width:170px;height:38px" role="img" aria-label="Line-drawn tropical leaves in mint and lilac"></div>
    <div class="edge-line" style="top:0"></div>
    <div class="edge-line" style="bottom:4px"></div>

    <div class="brand-dot" style="left:219px;top:13px;width:28px;height:28px"></div>
    <div class="brand-name" style="left:175px;top:52px;font-size:8px">Vesmor Herbal</div>

    <div class="title-script" style="left:0;right:0;top:70px;font-size:44px;color:var(--gold)">Amber Dew</div>
    <div class="centered" style="left:0;right:0;top:128px;font-size:9px;font-weight:400">FACIAL &amp; BODY OIL</div>
    <div class="centered" style="left:0;right:0;top:147px;font-size:6.5px;letter-spacing:.42em;color:var(--gold)">FOR ALL SKIN TYPE</div>

    <div class="copy copy--left">
      <p>Lorem ipsum dolor sit amet, consectetuer adipiscing elit, sed diam nonummy nibh euismod tincidunt ut laoreet dolore magna aliquam erat volutpat.</p>
      <p>Duis autem vel eum iriure dolor in hendrerit in vulputate velit esse molestie consequat, vel illum dolore eu feugiat nulla facilisis at vero eros et</p>
    </div>
    <div class="fine" style="left:104px;top:128px;width:36px">Lorem ipsum dolor sit amet, consectetuer adipiscing elit, sed diam nonummy</div>

    <div class="copy copy--right">
      <h4>Description</h4>
      <p>Lorem ipsum dolor sit amet, consectetuer adipiscing elit, sed diam nonummy nibh euismod tincidunt ut laoreet dolore magna aliquam erat volutpat.</p>
      <h4>Ingredients</h4>
      <p>Ut wisi enim ad minim veniam, quis nostrud exerci tation ullamcorper suscipit lobortis nisl ut aliquip ex ea commodo consequat.</p>
      <h4>Dirrection</h4>
      <p>Duis autem vel eum iriure dolor in hendrerit in vulputate velit esse molestie consequat, vel illum dolore eu feugiat nulla facilisis at vero eros</p>
    </div>

    <div class="tab" style="left:190px;top:190px;width:87px;height:15px;font-size:6.5px;line-height:15px">Net Wt. 30ml</div>
  </section>

  <!-- jar -->
  <div class="abs jar-lid"></div>
  <div class="abs jar-body"></div>

  <section class="label label--jar">
    <div class="foliage" style="left:0;top:0;width:360px;height:30px" role="img" aria-label="Line-drawn tropical leaves in mint and lilac"></div>
    <div class="foliage" style="right:0;top:0;width:360px;height:30px" role="img" aria-label="Line-drawn tropical leaves in mint and lilac"></div>
    <div class="foliage" style="left:30px;bottom:0;width:330px;height:22px" role="img" aria-label="Line-drawn tropical leaves in mint and lilac"></div>
    <div class="foliage" style="right:30px;bottom:0;width:330px;height:22px" role="img" aria-label="Line-drawn tropical leaves in mint and lilac"></div>
    <div class="edge-line" style="top:0"></div>
    <div class="edge-line" style="bottom:4px"></div>

    <div class="brand-dot" style="left:373px;top:12px;width:26px;height:26px"></div>
    <div class="brand-name" style="left:409px;top:15px;font-size:8px">Vesmor Herbal</div>

    <div class="title-script" style="left:0;right:0;top:34px;font-size:42px;color:var(--teal-dark)">Honey Drift</div>
    <div class="centered" style="left:0;right:0;top:91px;font-size:7px">Nourishing, Healing &amp; Moisturizing</div>
    <div class="centered" style="left:0;right:0;top:101px;font-size:7px;letter-spacing:.45em;color:var(--sky)">HANDCRAFTED</div>
    <div class="centered" style="left:0;right:0;top:122px;font-size:5px">Enriched with Rosehip Oil</div>

    <div class="fine" style="left:44px;top:91px;width:102px">Lorem ipsum dolor sit amet, consectetuer adipiscing elit, sed diam nonummy nibh euismod</div>

    <div class="copy copy--mid">
      <p>Lorem ipsum dolor sit amet, consectetuer adipiscing elit, sed diam nonummy nibh euismod tincidunt ut laoreet dolore magna aliquam erat volutpat.</p>
      <p>Duis autem vel eum iriure dolor in hendrerit in vulputate velit esse molestie consequat, vel illum dolore eu feugiat nulla facilisis at vero eros et accumsan et iusto odio dignissim qui blandit praesent luptatum zzril delenit augue duis dolore te feugait nulla</p>
    </div>

    <div class="copy copy--right">
      <h4>Description</h4>
      <p>Lorem ipsum dolor sit amet, consectetuer adipiscing elit, sed diam nonummy nibh euismod tincidunt ut laoreet dolore magna aliquam erat volutpat.</p>
      <h4>Ingredients</h4>
      <p>Ut wisi enim ad minim veniam, quis nostrud exerci tation ullamcorper suscipit lobortis nisl ut aliquip ex ea commodo consequat.</p>
      <h4>Dirrection</h4>
      <p>Duis autem vel eum iriure dolor in hendrerit in vulputate velit esse molestie consequat, vel illum dolore eu feugiat nulla facilisis at vero eros et accumsan et iusto odio dignissim qui blandit praesent luptatum zzril delenit augue duis dolore te feugait nulla</p>
    </div>

    <div class="tab" style="left:395px;top:137px;width:106px;height:12px;font-size:6.5px;line-height:12px">200gr of Goodness</div>
  </section>

  <!-- lid label -->
  <section class="label label--lid">
    <div class="lid-foliage" role="img" aria-label="Ring of line-drawn tropical leaves in mint and lilac"></div>
    <div class="brand-dot" style="left:114px;top:20px;width:42px;height:42px"></div>
    <div class="brand-name" style="left:0;right:0;top:71px;font-size:8px;text-align:center">Vesmor Herbal</div>
    <div class="title-script" style="left:0;right:0;top:100px;font-size:54px;color:var(--teal-dark)">Honey Drift</div>
    <div class="centered" style="left:0;right:0;top:160px;font-size:9.5px">Nourishing, Healing &amp; Moisturizing</div>
    <div class="centered" style="left:0;right:0;top:176px;font-size:11.5px;letter-spacing:.5em;color:var(--sky);padding-left:.5em">HANDCRAFTED</div>
    <div class="centered" style="left:0;right:0;top:196px;font-size:8px">Enriched with Rosehip Oil</div>
  </section>

</body>
</html>
```